Qasrwen hotel

Kindly design a profile for our hotel, you an find attached the original profile witch needs a lot of work and alteration, kindly upgrade the design to be more professional. And you can find attached the logo (you are welcome to play with it).

```html
<!DOCTYPE html>
<html lang="en">
<head>
<meta charset="UTF-8">
<title>Qasrwen Hotel – Room Facilities</title>
<link rel="stylesheet" href="https://fonts.googleapis.com/css2?family=Jost:wght@400;500&family=Carlito&family=Arimo&display=swap">
<style>
  :root {
    --page: #ffffff;
    --ink: #000000;
    --text: #111111;
    --room-warm: #8a8278;
    --room-light: #c9c4bc;
    --room-dark: #4a4744;
  }
  * { margin: 0; padding: 0; box-sizing: border-box; }
  html, body { width: 1200px; height: 902px; overflow: hidden; background: var(--page); }
  .page { position: relative; width: 1200px; height: 902px; background: var(--page); }

  .spine { position: absolute; left: 92px; width: 4px; background: var(--ink); }
  .spine--top { top: 0; height: 111px; }
  .spine--bottom { top: 234px; height: 654px; }

  .brand-tag {
    position: absolute; left: 94px; top: 173px;
    transform: translate(-50%, -50%) rotate(-90deg);
    font-family: "Arimo", Arial, sans-serif; font-size: 15px; letter-spacing: 0.5px;
    color: var(--ink); white-space: nowrap;
  }

  .section-title {
    position: absolute; left: 154px; top: 176px;
    font-family: "Jost", "Futura", sans-serif; font-weight: 400;
    font-size: 88px; line-height: 94px; color: var(--ink);
  }

  .facility-list {
    position: absolute; right: 671px; top: 432px; list-style: none; text-align: right;
    font-family: "Carlito", "Calibri", sans-serif; font-size: 29px; line-height: 43.5px; color: var(--text);
  }

  .room-photo { position: absolute; left: 617px; width: 528px; height: 297px; }
  .room-photo--suite {
    top: 160px;
    background: linear-gradient(180deg, var(--room-light) 0%, var(--room-warm) 55%, var(--room-dark) 100%);
  }
  .room-photo--bedroom {
    top: 484px;
    background: linear-gradient(180deg, var(--room-light) 0%, var(--room-warm) 50%, var(--room-dark) 100%);
  }
</style>
</head>
<body>
  <main class="page">
    <div class="spine spine--top"></div>
    <div class="spine spine--bottom"></div>
    <div class="brand-tag">QASRWEN</div>

    <h1 class="section-title">Room<br>Facilities.</h1>

    <ul class="facility-list">
      <li>Air conditioning</li>
      <li>Satellite TV (flat screen)</li>
      <li>Mind fridge</li>
      <li>Radio</li>
      <li>Seating area</li>
      <li>Phone</li>
    </ul>

    <div class="room-photo room-photo--suite" role="img" aria-label="Hotel suite interior with bed, wall-mounted flat screen TV, cove lighting and a small dining table"></div>
    <div class="room-photo room-photo--bedroom" role="img" aria-label="Hotel bedroom with dark bedspread, framed wall art, curtained window and a seating area with round table"></div>
  </main>
</body>
</html>
```